Need Letterhead and Business Card

I have a logo but i need new letterhead and biz cards. We are a real estate investment firm so we need very professional but also do not want to be old fashioned. We have 3 locations; Singapore, New York and Ponte Vedra Florida. I can provide full addresses if needed. If you have adjustments to our logo you would recommend we are open to them.
I will be putting in a separate project but we also need a template for our own powerpoint slide presentations and website.

Industry/Entity Type

Real Estate

```html
<!DOCTYPE html>
<html lang="en">
<head>
<meta charset="utf-8">
<title>Varelth Letterhead Options</title>
<link href="https://fonts.googleapis.com/css2?family=Carlito:wght@400;700&family=Exo+2:wght@400&display=swap" rel="stylesheet">
<style>
  :root {
    --board: #231f20;
    --paper: #ffffff;
    --navy: #0a4f86;
    --brand: #1d4f82;
    --gold: #d9a21b;
    --ink: #444444;
    --muted: #9a9a9a;
    --wash: #f6f7f8;
  }
  * { box-sizing: border-box; margin: 0; padding: 0; }
  html, body { width: 1200px; height: 1000px; overflow: hidden; }
  body {
    background: var(--board);
    font-family: "Carlito", "Calibri", sans-serif;
    color: var(--ink);
    position: relative;
  }
  .sheet {
    position: absolute;
    width: 520px;
    height: 670px;
    background: var(--paper);
    overflow: hidden;
  }
  .sheet--one { left: 69px; top: 183px; }
  .sheet--two { left: 628px; top: 178px; width: 519px; }
  .edge-bar {
    position: absolute; left: 0; top: 0;
    width: 5px; height: 87px;
    background: var(--navy);
  }
  .brand {
    position: absolute; top: 30px;
    font-weight: 700; font-size: 30px;
    color: var(--brand); letter-spacing: 0.5px; line-height: 1;
  }
  .sheet--one .brand { left: 24px; }
  .sheet--two .brand { left: 0; width: 100%; text-align: center; top: 26px; }
  .contact {
    position: absolute; left: 368px; top: 20px;
    font-size: 6.5px; line-height: 6.6px; color: var(--muted);
  }
  .contact li { list-style: none; display: flex; align-items: center; gap: 4px; }
  .contact svg { width: 6px; height: 6px; fill: var(--gold); flex: none; }
  .wash {
    position: absolute; top: 116px;
    width: 460px; height: 335px;
    background: linear-gradient(120deg, var(--paper) 20%, var(--wash) 60%, var(--paper) 95%);
  }
  .sheet--one .wash { left: 26px; }
  .sheet--two .wash { left: 36px; top: 122px; }
  .letter { position: absolute; width: 445px; font-size: 8.6px; line-height: 11.7px; }
  .sheet--one .letter { left: 28px; top: 122px; }
  .sheet--two .letter { left: 37px; top: 129px; }
  .date, .recipient, .address { font-size: 9.6px; line-height: 13px; }
  .recipient { font-weight: 700; margin-top: 13px; }
  .address { margin-top: 10px; }
  .body { margin-top: 36px; }
  .body p { text-align: justify; margin-bottom: 12px; }
  .closing { position: absolute; font-size: 12.5px; color: #555; }
  .sheet--one .closing { left: 31px; top: 464px; }
  .sheet--two .closing { left: 39px; top: 471px; }
  .signature-area {
    position: absolute; width: 186px; height: 115px;
    background: linear-gradient(180deg, #fafafa, #f1f1f1);
  }
  .sheet--one .signature-area { left: 20px; top: 457px; }
  .sheet--two .signature-area { left: 29px; top: 467px; }
  .footer {
    position: absolute; left: 0; bottom: 0;
    width: 100%; height: 40px;
    background: var(--navy); color: #e6eef6;
    text-align: center;
  }
  .footer .web { font-size: 7.5px; letter-spacing: 2px; }
  .sheet--one .footer .web { line-height: 46px; }
  .footer .lines { padding-top: 6px; font-size: 6.5px; line-height: 7px; }
  .sheet--two .footer .web { font-size: 6.5px; letter-spacing: 1.2px; margin-top: 2px; }
  .caption {
    position: absolute; width: 300px; text-align: center;
    font-family: "Exo 2", "Play", sans-serif; font-size: 15px; color: #ffffff;
  }
  .caption--one { left: 180px; top: 880px; }
  .caption--two { left: 737px; top: 876px; }
</style>
</head>
<body>

<svg width="0" height="0" style="position:absolute" aria-hidden="true">
  <symbol id="i-home" viewBox="0 0 10 10"><path d="M5 1 0 5h1.5v4h2.5V6.5h2V9h2.5V5H10z"/></symbol>
  <symbol id="i-mobile" viewBox="0 0 10 10"><rect x="3" y="0.5" width="4" height="9" rx="0.8"/></symbol>
  <symbol id="i-phone" viewBox="0 0 10 10"><path d="M2 1l2 2-1 1.5c.8 1.5 1.8 2.5 3.3 3.3L7.8 6.8l2 2L8.5 10C4 9.5.5 6 0 1.5z"/></symbol>
  <symbol id="i-mail" viewBox="0 0 10 10"><rect x="0.5" y="2" width="9" height="6"/></symbol>
</svg>

<section class="sheet sheet--one">
  <div class="edge-bar"></div>
  <div class="brand">VARELTH</div>
  <ul class="contact">
    <li><svg><use href="#i-home"/></svg>9999, Address Line, Your City</li>
    <li><svg></svg>Your State , Zip Code - 100 001</li>
    <li><svg><use href="#i-mobile"/></svg>+ 123 456 789</li>
    <li><svg><use href="#i-phone"/></svg>+ 123 456 789</li>
    <li><svg><use href="#i-phone"/></svg>+ 123 456 789</li>
    <li><svg><use href="#i-mail"/></svg>info@varelthestates.com</li>
  </ul>
  <div class="wash"></div>
  <article class="letter">
    <div class="date">Date</div>
    <div class="recipient">Recipient Name</div>
    <div class="address">Company Name<br>Street Address<br>City, State, Zip</div>
    <div class="body">
      <p>Lorem ipsum dolor sit amet, consectetuer adipiscing elit, sed diam nonummy nibh euismod tincidunt ut laoreet dolore magna aliquam erat volutpat. Ut wisi enim ad minim veniam, quis nostrud exerci tation ullamcorper suscipit lobortis nisl ut aliquip ex ea commodo consequat. Duis autem vel eum iriure dolor in hendrerit in vulputate velit esse molestie consequat, vel illum dolore eu feugiat.</p>
      <p>nulla facilisis at vero eros et accumsan et iusto odio dignissim qui blandit praesent luptatum zzril delenit augue duis dolore te feugait nulla facilisi. Nam liber tempor cum soluta nobis eleifend option congue nihil imperdiet doming id quod mazim placerat facer possim assum. Typi non habent claritatem insitam; est usus legentis in iis qui facit eorum claritatem. Investigationes demonstraverunt lectores.</p>
      <p>legere me lius quod ii legunt saepius. Claritas est etiam processus dynamicus, qui sequitur mutationem consuetudium lectorum. Mirum est notare quam littera gothica, quam nunc putamus parum claram, anteposuerit litterarum formas humanitatis per seacula quarta decima et quinta decima. Eodem modo typi, qui nunc nobis videntur parum clari, fiant sollemnes in futurum.</p>
      <p>legere me lius quod ii legunt saepius. Claritas est etiam processus dynamicus, qui sequitur mutationem consuetudium lectorum.</p>
    </div>
  </article>
  <div class="signature-area" role="img" aria-label="Handwritten signature"></div>
  <div class="closing">Sincerely,</div>
  <footer class="footer"><div class="web">www.varelthestates.com</div></footer>
</section>

<section class="sheet sheet--two">
  <div class="edge-bar"></div>
  <div class="brand">VARELTH</div>
  <div class="wash"></div>
  <article class="letter">
    <div class="date">Date</div>
    <div class="recipient">Recipient Name</div>
    <div class="address">Company Name<br>Street Address<br>City, State, Zip</div>
    <div class="body">
      <p>Lorem ipsum dolor sit amet, consectetuer adipiscing elit, sed diam nonummy nibh euismod tincidunt ut laoreet dolore magna aliquam erat volutpat. Ut wisi enim ad minim veniam, quis nostrud exerci tation ullamcorper suscipit lobortis nisl ut aliquip ex ea commodo consequat. Duis autem vel eum iriure dolor in hendrerit in vulputate velit esse molestie consequat, vel illum dolore eu feugiat.</p>
      <p>nulla facilisis at vero eros et accumsan et iusto odio dignissim qui blandit praesent luptatum zzril delenit augue duis dolore te feugait nulla facilisi. Nam liber tempor cum soluta nobis eleifend option congue nihil imperdiet doming id quod mazim placerat facer possim assum. Typi non habent claritatem insitam; est usus legentis in iis qui facit eorum claritatem. Investigationes demonstraverunt lectores.</p>
      <p>legere me lius quod ii legunt saepius. Claritas est etiam processus dynamicus, qui sequitur mutationem consuetudium lectorum. Mirum est notare quam littera gothica, quam nunc putamus parum claram, anteposuerit litterarum formas humanitatis per seacula quarta decima et quinta decima. Eodem modo typi, qui nunc nobis videntur parum clari, fiant sollemnes in futurum.</p>
      <p>legere me lius quod ii legunt saepius. Claritas est etiam processus dynamicus, qui sequitur mutationem consuetudium lectorum.</p>
    </div>
  </article>
  <div class="signature-area" role="img" aria-label="Handwritten signature"></div>
  <div class="closing">Sincerely,</div>
  <footer class="footer">
    <div class="lines">
      9999, Address Line, Your City, Your State , Zip Code - 100 001<br>
      + 123 456 789 &nbsp; + 123 456 789 &nbsp; + 123 456 789<br>
      info@varelthestates.com
    </div>
    <div class="web">www.varelthestates.com</div>
  </footer>
</section>

<div class="caption caption--one">Letterhead Option_01</div>
<div class="caption caption--two">Letterhead Option_02</div>

</body>
</html>
```